Korelith InsurTech Website Redesign - 10 Pages

Design a modern, professional website for Korelith, an AI-native cyber insurance platform serving SMBs.

DELIVERABLE: 10 pages (desktop + mobile mockups)
- Homepage (priority #1)
- 4 Platform pages (Cyber Insurance, Brokers, Underwriters, Policyholder)
- 3 Company pages (About Us, Team, Contact/Careers)
- 2 Risk pages (AI Risk, Cyber Risk)

DESIGN DIRECTION:
- Professional + innovative (insurance meets technology)
- Trust-building + modern aesthetic
- Reference: Brambury Insurance, Tidewick Insurance
- Use official brand colors (6-color palette provided)
- Avoid generic security clipart (padlocks, shields, magnifying glasses)
- Custom graphics, not AI-generated or stock imagery

CURRENT SITES FOR REFERENCE:
- www.korelith.ai
- https://a3c9124d.korelith-website.vorlapages.dev/

Full detailed brief with all content, page specifications, and brand guidelines attached as PDF (Korelith_PixelHarbor_Brief.pdf).

TARGET AUDIENCE: Insurance brokers (primary), SMB business owners (secondary)
KEY MESSAGE: "Cyber Insurance the Way It Should Be"

Additional brand assets available in Google Drive - link provided on request.

```html
<!DOCTYPE html>
<html lang="en">
<head>
<meta charset="utf-8">
<title>Korelith — Cyber Insurance</title>
<link href="https://fonts.googleapis.com/css2?family=Inter:wght@400;600;700&display=swap" rel="stylesheet">
<style>
:root{
  --white:#ffffff;
  --ink:#111827;
  --muted:#4b5563;
  --soft-bg:#f7f8fa;
  --chip-bg:#e4e6e9;
  --chip-text:#a7adb5;
  --navy-1:#1a2851;
  --navy-2:#1e3163;
  --footer-bg:#0f1729;
  --footer-text:#c9cfe0;
  --footer-line:#222c44;
  --accent:#1aa3e8;
}
*{margin:0;padding:0;box-sizing:border-box}
html,body{width:1200px;height:904px;overflow:hidden}
body{font-family:"Inter",Arial,sans-serif;background:var(--white);color:var(--ink);position:relative}
section,footer{position:absolute;left:0;width:1200px}
.center-x{position:absolute;left:518px;transform:translateX(-50%);text-align:center;white-space:nowrap}

.foundations{top:0;height:248px;background:var(--white)}
.foundations .section-title{top:28px;font-size:21px;font-weight:700}
.pillar{position:absolute;top:103px;width:160px;transform:translateX(-50%);text-align:center}
.pillar h3{font-size:12.5px;font-weight:700;margin-bottom:8px}
.pillar p{font-size:10.3px;line-height:17px;color:var(--muted)}

.integrations{top:248px;height:235px;background:var(--soft-bg)}
.integrations .section-title{top:56px;font-size:21px;font-weight:700}
.integrations .lead{top:112px;font-size:10.3px;color:var(--muted)}
.chip{position:absolute;top:156px;width:79px;height:26px;background:var(--chip-bg);color:var(--chip-text);font-size:12px;display:flex;align-items:center;justify-content:center}

.cta{top:483px;height:240px;background:linear-gradient(180deg,var(--navy-1),var(--navy-2))}
.cta .cta-title{top:55px;font-size:22px;font-weight:700;color:var(--white)}
.cta .cta-text{top:97px;font-size:10.3px;line-height:17px;color:#dfe4f1}
.cta .demo-button{position:absolute;left:459px;top:152px;width:119px;height:35px;background:var(--accent);color:var(--white);font-size:10.5px;font-weight:600;border-radius:3px;display:flex;align-items:center;justify-content:center;text-decoration:none}

.site-footer{top:723px;height:181px;background:var(--footer-bg);color:var(--footer-text)}
.footer-col{position:absolute;top:39px}
.footer-col h4{font-size:10.5px;font-weight:700;color:var(--white);margin-bottom:8px}
.footer-col.brand h4{font-size:12px}
.footer-col p{font-size:10.3px;line-height:17px;width:165px}
.footer-col ul{list-style:none}
.footer-col li{font-size:9.5px;line-height:17px}
.footer-rule{position:absolute;top:143px;left:0;width:1200px;height:1px;background:var(--footer-line)}
.copyright{position:absolute;top:152px;left:518px;transform:translateX(-50%);font-size:9px;color:#8a93a8;white-space:nowrap}
</style>
</head>
<body>
<section class="foundations">
  <h2 class="section-title center-x">Built on Strong Foundations</h2>
  <div class="pillar" style="left:216px"><h3>Security &amp; Compliance</h3><p>Enterprise-grade protection and regulatory compliance at every layer.</p></div>
  <div class="pillar" style="left:417px"><h3>AI Intelligence</h3><p>Advanced analytics and predictive models for smarter risk decisions.</p></div>
  <div class="pillar" style="left:619px"><h3>Automation</h3><p>Streamlined workflows that reduce manual effort and operational costs.</p></div>
  <div class="pillar" style="left:820px"><h3>Scalability</h3><p>A cloud-native platform designed to grow with your business.</p></div>
</section>

<section class="integrations">
  <h2 class="section-title center-x">Seamless Integrations</h2>
  <p class="lead center-x">Connect effortlessly with your existing systems, data sources, and enterprise tools.</p>
  <div class="chip" style="left:270px">CRM</div>
  <div class="chip" style="left:375px">Cloud</div>
  <div class="chip" style="left:480px">API</div>
  <div class="chip" style="left:585px">Security</div>
  <div class="chip" style="left:690px">Analytics</div>
</section>

<section class="cta">
  <h2 class="cta-title center-x">Ready to Transform Your Insurance Operations?</h2>
  <p class="cta-text center-x">Discover how Korelith can streamline underwriting, enhance risk intelligence, and<br>secure your digital future.</p>
  <a class="demo-button" href="#">Request a Demo</a>
</section>

<footer class="site-footer">
  <div class="footer-col brand" style="left:159px"><h4>Korelith</h4><p>AI-powered cyber insurance and risk intelligence for the modern enterprise.</p></div>
  <div class="footer-col" style="left:345px"><h4>Platform</h4><ul><li>Cyber Insurance</li><li>For Brokers</li><li>Risk Intelligence</li></ul></div>
  <div class="footer-col" style="left:531px"><h4>Company</h4><ul><li>About</li><li>Contact</li><li>Careers</li></ul></div>
  <div class="footer-col" style="left:719px"><h4>Legal</h4><ul><li>Privacy Policy</li><li>Terms of Service</li><li>Compliance</li></ul></div>
  <div class="footer-rule"></div>
  <p class="copyright">© 2026 Korelith. All rights reserved.</p>
</footer>
</body>
</html>
```